Infographic job advert for modern Project Management company in renewables

I want a modern eye catching infographic style job advert . The role isnt clearly defined and so I want the add to focus on qualities and expereince so i cast a broad net and see who is interested. I have an example add from Veltrax inthe brief, this is just something I found , but I'm open to better ideas, layouts etc. There is a document for some key works, valuses etc. I have included out logo files etc . Also our website is www.marondltd.example , this tells you more about the company plus you will find us on pinglehub. reading someof our posts might help. I want modern, and eye catching. I also want the end produc to be editable by myslef for future roles or if I need to try again to get the right people. The add will get posted on Pinglehub mainly.

Target Market(s)

Experienced professionals

Industry/Entity Type

Project Management, UK based, Client Project Manager

Font styles to use
Sans Serif

Requirements
Must have
• Modern, Eye catching, editable, easy to understand, and intersting
Nice to have
• Open to ideas
Should not have
• Not specific roles, no mention of package

```html
<!DOCTYPE html>
<html lang="en">
<head>
<meta charset="utf-8">
<title>Project Management Roles – Marond</title>
<link href="https://fonts.googleapis.com/css2?family=Outfit:wght@400;500;600;700&display=swap" rel="stylesheet">
<style>
  :root {
    --page: #ffffff;
    --board: #f2f1f1;
    --frame: #9a9a9a;
    --brand-ink: #2f2f33;
    --header-dark: #6a1018;
    --header-mid: #9c1c27;
    --header-light: #d0303c;
    --culture: #e1333f;
    --values: #ee636b;
    --potential: #cf6068;
    --wants: #d2303d;
    --donts: #5e5e5e;
    --text: #ffffff;
    --bullet: #f7c9cc;
    --icon-zone: rgba(255,255,255,0.14);
  }
  * { margin: 0; padding: 0; box-sizing: border-box; }
  html, body { width: 1200px; height: 1000px; overflow: hidden; background: var(--page); }
  body { font-family: 'Outfit', sans-serif; position: relative; }

  .advert {
    position: absolute; left: 145px; top: 249px; width: 963px; height: 504px;
    border: 1px solid var(--frame); background: var(--board);
  }
  .brand {
    position: absolute; left: 0; top: 0; width: 258px; height: 86px; background: #fff;
    display: flex; align-items: center; padding-left: 18px;
  }
  .brand-name { font-size: 40px; font-weight: 600; color: var(--brand-ink); line-height: 1; }

  .banner {
    position: absolute; left: 258px; top: 0; width: 704px; height: 86px;
    background: linear-gradient(90deg, var(--header-dark) 0%, var(--header-mid) 50%, var(--header-light) 100%);
  }
  .banner-photo {
    position: absolute; right: 0; top: 0; width: 300px; height: 86px;
    background: linear-gradient(90deg, rgba(208,48,60,0) 0%, rgba(226,70,78,0.7) 60%, rgba(200,40,50,0.8) 100%);
  }
  .banner-title {
    position: absolute; left: 16px; top: 28px; color: var(--text);
    font-size: 33px; font-weight: 700; letter-spacing: -0.4px; line-height: 1; white-space: nowrap;
  }
  .banner-title .region { font-size: 19px; font-weight: 600; margin-left: 8px; }
  .banner-pin { position: absolute; left: 506px; top: 0; }
  .follow {
    position: absolute; right: 12px; top: 20px; width: 70px; text-align: center; color: var(--text);
  }
  .follow-network { font-size: 11px; font-weight: 700; display: block; margin-bottom: 14px; }
  .follow-label { font-size: 11px; font-weight: 700; }
  .credit { position: absolute; right: 6px; bottom: 5px; font-size: 4px; color: rgba(255,255,255,0.7); }

  .panel { position: absolute; top: 96px; height: 398px; color: var(--text); }
  .panel-culture   { left: 22px;  width: 184px; background: var(--culture); }
  .panel-values    { left: 206px; width: 184px; background: var(--values); border-left: 1px solid #fff; }
  .panel-potential { left: 391px; width: 182px; background: var(--potential); border-left: 1px solid #fff; }
  .panel-wants     { left: 574px; width: 184px; background: var(--wants); border-left: 1px solid #fff; }
  .panel-donts     { left: 759px; width: 183px; background: var(--donts); border-left: 1px solid #fff; }

  .panel-icon {
    position: absolute; left: 34px; top: 30px; width: 116px; height: 126px;
    border-radius: 50px 50px 20px 20px; background: var(--icon-zone);
  }
  .panel-heading { position: absolute; top: 166px; font-size: 18px; font-weight: 600; line-height: 22px; }
  .panel-list { position: absolute; list-style: none; font-size: 14.5px; line-height: 19px; }
  .panel-list li { position: relative; padding-left: 11px; margin-bottom: 8px; }
  .panel-list li::before {
    content: ""; position: absolute; left: 0; top: 6px; width: 6px; height: 6px; background: var(--bullet);
  }
  .panel-culture .panel-heading { left: 29px; }
  .panel-culture .panel-list { left: 21px; top: 196px; }
  .panel-values .panel-heading { left: 27px; }
  .panel-values .panel-list { left: 18px; top: 196px; }
  .panel-potential .panel-heading { left: 26px; }
  .panel-potential .panel-list { left: 17px; top: 196px; width: 135px; }
  .panel-wants .panel-heading { left: 15px; }
  .panel-wants .panel-list { left: 11px; top: 196px; }
  .panel-donts .panel-heading { left: 24px; }
  .panel-donts .panel-list { left: 23px; top: 219px; }

  .joints { position: absolute; left: 0; top: 0; pointer-events: none; }
</style>
</head>
<body>
  <section class="advert">
    <div class="brand">
      <span class="brand-name">Marond</span>
    </div>

    <header class="banner">
      <div class="banner-photo" role="img" aria-label="Photo of hands joined together in red tones"></div>
      <h1 class="banner-title">Project Management Roles<span class="region">UK wide</span></h1>
      <svg class="banner-pin" width="100" height="86" viewBox="0 0 100 86" aria-hidden="true">
        <g fill="none" stroke="rgba(255,255,255,0.55)" stroke-width="1">
          <circle cx="40" cy="42" r="16"/>
          <circle cx="40" cy="42" r="26"/>
          <circle cx="40" cy="42" r="36"/>
        </g>
        <path d="M40 72 C33 60 28 54 28 46 a12 12 0 0 1 24 0 c0 8 -5 14 -12 26z" fill="#f3d6d8"/>
        <circle cx="40" cy="46" r="5" fill="#9c1c27"/>
      </svg>
      <div class="follow">
        <span class="follow-network">Pinglehub</span>
        <span class="follow-label">Follow Us</span>
      </div>
      <span class="credit">Image: stock library</span>
    </header>

    <article class="panel panel-culture">
      <div class="panel-icon" role="img" aria-label="Line icon of a head profile with overlapping circles"></div>
      <h2 class="panel-heading">Culture:</h2>
      <ul class="panel-list">
        <li>Relaxed</li><li>Hardworking</li><li>Open to ideas</li><li>Focused on results</li>
      </ul>
    </article>

    <article class="panel panel-values">
      <div class="panel-icon" role="img" aria-label="Line icon of a head profile with a balance symbol"></div>
      <h2 class="panel-heading">Values</h2>
      <ul class="panel-list">
        <li>Integrity</li><li>Quality</li><li>Communication</li><li>Detail</li>
      </ul>
    </article>

    <article class="panel panel-potential">
      <div class="panel-icon" role="img" aria-label="Line icon of a head profile with a puzzle piece"></div>
      <h2 class="panel-heading">Potential:</h2>
      <ul class="panel-list">
        <li>Define your role</li><li>Enjoy your job</li>
        <li>What you put in shapes what you get back</li><li>Shape the business</li>
      </ul>
    </article>

    <article class="panel panel-wants">
      <div class="panel-icon" role="img" aria-label="Line icon of a head profile with a paper bird"></div>
      <h2 class="panel-heading">Things we want:</h2>
      <ul class="panel-list">
        <li>Thinkers</li><li>Doers</li><li>Listeners</li><li>Attention to details</li>
        <li>Team players</li><li>Embraces a challenge</li><li>Can do people</li>
      </ul>
    </article>

    <article class="panel panel-donts">
      <div class="panel-icon" role="img" aria-label="Line icon of a head profile with a storm cloud"></div>
      <h2 class="panel-heading">What we<br>don’t want:</h2>
      <ul class="panel-list">
        <li>Tell me what to do</li><li>That’s not my job</li><li>It doesn’t matter</li><li>I’ll get round to it</li>
      </ul>
    </article>

    <svg class="joints" width="963" height="504" viewBox="0 0 963 504" aria-hidden="true">
      <circle cx="222" cy="231" r="17" fill="var(--culture)" stroke="#fff" stroke-width="1"/>
      <rect x="204" y="213" width="2.5" height="36" fill="var(--culture)"/>
      <circle cx="407" cy="231" r="17" fill="var(--values)" stroke="#fff" stroke-width="1"/>
      <rect x="389" y="213" width="2.5" height="36" fill="var(--values)"/>
      <circle cx="590" cy="231" r="17" fill="var(--potential)" stroke="#fff" stroke-width="1"/>
      <rect x="572" y="213" width="2.5" height="36" fill="var(--potential)"/>
      <circle cx="775" cy="231" r="16" fill="#ffffff"/>
    </svg>
  </section>
</body>
</html>
```